Label Design for Climbing Chalk (fitness category)

I am looking for someone to design a front and back label for a bottle of liquid chalk. Liquid chalk is used in gyms, gymnastics, climbing to prevent your hands from getting moist and increase friction. I'm uploading some design motivations that I like.

The bottle is going to be black and I want the label to be clear. You have free reign of how you want to approach this design. Below are more specifics for the sizing:

*Attached is a picture of a competitor product (Tor Hold Liquid Chalk). Please don't use this for motivation, their label is very bad. I'm attaching a picture so that you can see what the bottle looks like.
*Attached are design motivations that I like
*The bottle is 50 ml, it's 3.75 inches tall, 2 inches wide and 1.25 inches in depth.
*The label can be square or oval (it's up to you). The size of the label needs to be 1,25 x 2.25 inches.
*Name of the product: Varnel Liquid Chalk
*Label needs to have the following Required Text. You can arrange it however you like:
- (50 ml)
- Made by USA Competitive Athletes for Athletes. Increases grip and lasts 3-4 times longer than regular chalk.
- Directions: Shake well. Squeeze some Varnel Liquid Chalk into your hand and rub your hands together. Let your hands air dry for about 10 seconds. To remove the chalk wash your hands with light soap.
Warning: Avoid contact with Eyes. Do not use on broken skin. Do not ingest. Keep out of reach of small children.
- Ingredients: Magnesium carbonate, SD Alcohol, hydroxypropylcellulose, colophonium.

Target Market(s)

Fitness, Athletes, Rock Climbers, Weight Lifters, Gymnasts, etc

Industry/Entity Type

Fitness

Font styles to use
Sans Serif

Colors

Designer to choose colors to be used in the design.

Requirements
Must have
• Please see Project Description for required text. The bottle is going to be black and I want the clear label so please be creative with the colors that would look good
Nice to have
• Please see attached branding ideas that I liked for font and colors. You don't have to strictly stick to them, these are just some of the ones I liked. Be creative and put your best foot forward.

```html
<!DOCTYPE html>
<html lang="en">
<head>
<meta charset="utf-8">
<title>Varnel Liquid Chalk – Clear Labels</title>
<link rel="stylesheet" href="https://fonts.googleapis.com/css2?family=Open+Sans:wght@600;700;800&display=swap">
<style>
  :root {
    --backdrop: #aebccd;
    --label-fill: rgba(255, 255, 255, 0.07);
    --label-edge: rgba(255, 255, 255, 0.75);
    --ink: #ffffff;
    --ink-soft: rgba(255, 255, 255, 0.92);
    --speckle-tone: rgba(255, 255, 255, 0.22);
  }
  * { box-sizing: border-box; margin: 0; padding: 0; }
  html, body {
    width: 1200px;
    height: 718px;
    overflow: hidden;
    background: var(--backdrop);
    font-family: "Open Sans", Arial, sans-serif;
    color: var(--ink);
  }
  .label-sheet {
    position: relative;
    width: 1200px;
    height: 718px;
  }
  .label {
    position: absolute;
    top: 79px;
    width: 304px;
    height: 560px;
    border: 1.5px solid var(--label-edge);
    border-radius: 26px;
    background: var(--label-fill);
  }
  .label--front { left: 276px; }
  .label--back  { left: 620px; }

  /* brand wordmark */
  .brand-name {
    font-weight: 800;
    color: var(--ink);
    line-height: 0.9;
  }
  .label--front .brand-name {
    position: absolute;
    left: 24px;
    top: 40px;
  }
  .brand-name__line { display: block; }
  .label--front .brand-name__line { font-size: 62px; letter-spacing: -1px; }
  .label--front .brand-name__line--chalk {
    font-size: 40px;
    letter-spacing: 3px;
    margin-top: 12px;
  }

  .tagline {
    position: absolute;
    left: 24px;
    top: 290px;
    width: 270px;
    font-size: 16px;
    font-weight: 700;
    line-height: 1.4;
  }
  .claim {
    position: absolute;
    left: 24px;
    top: 342px;
    width: 256px;
    font-size: 12.5px;
    font-weight: 600;
    line-height: 1.45;
    color: var(--ink-soft);
  }
  .speckle-field {
    position: absolute;
    border-radius: 0 0 24px 24px;
    background: radial-gradient(ellipse at 55% 40%, var(--speckle-tone), rgba(255,255,255,0) 70%);
  }
  .label--front .speckle-field {
    left: 14px;
    right: 14px;
    top: 395px;
    height: 125px;
  }
  .net-volume {
    position: absolute;
    left: 0;
    right: 0;
    top: 525px;
    text-align: center;
    font-size: 16px;
    font-weight: 700;
  }

  /* back label copy */
  .copy-block {
    position: absolute;
    left: 24px;
    width: 258px;
    color: var(--ink-soft);
  }
  .copy-block h2 {
    font-size: 12.5px;
    font-weight: 700;
    margin-bottom: 5px;
  }
  .copy-block p {
    font-size: 11.4px;
    font-weight: 600;
    line-height: 1.5;
  }
  .copy-block--directions p { text-align: justify; }
  .copy-block--directions  { top: 62px; }
  .copy-block--warning     { top: 180px; }
  .copy-block--ingredients { top: 272px; }

  .back-brand {
    position: absolute;
    left: 18px;
    top: 372px;
    display: flex;
    align-items: stretch;
    gap: 10px;
  }
  .back-brand .brand-name__line { font-size: 36px; letter-spacing: -0.5px; }
  .back-brand .brand-name__line--chalk {
    font-size: 24px;
    letter-spacing: 2px;
    margin-top: 8px;
  }
  .back-brand__rule {
    width: 2px;
    background: var(--ink);
  }
  .label--back .speckle-field {
    left: 150px;
    right: 14px;
    top: 380px;
    height: 165px;
  }
</style>
</head>
<body>
<main class="label-sheet">

  <section class="label label--front" aria-label="Front label">
    <h1 class="brand-name">
      <span class="brand-name__line">Varnel</span>
      <span class="brand-name__line">liquid</span>
      <span class="brand-name__line brand-name__line--chalk">CHALK</span>
    </h1>
    <p class="tagline">Made by USA Competitive Athletes for Athletes.</p>
    <p class="claim">Increases grip and lasts 3-4 times longer than regular chalk.</p>
    <div class="speckle-field" role="img" aria-label="Scattered white dot pattern"></div>
    <p class="net-volume">NET : 50 ml</p>
  </section>

  <section class="label label--back" aria-label="Back label">
    <div class="copy-block copy-block--directions">
      <h2>DIRECTIONS:</h2>
      <p>Shake well. Squeeze some Varnel Liquid Chalk into your hand and rub your hands together. Let your hands air dry for about 10 seconds. To remove the chalk wash your hands with light soap.</p>
    </div>
    <div class="copy-block copy-block--warning">
      <h2>WARNING :</h2>
      <p>Avoid contact with Eyes. Do not use on broken skin. Do not ingest. Keep out of reach of small children.</p>
    </div>
    <div class="copy-block copy-block--ingredients">
      <h2>INGREDIENTS :</h2>
      <p>Magnesium carbonate, SD Alcohol, hydroxypropylcellulose, colophonium.</p>
    </div>

    <div class="speckle-field" role="img" aria-label="Scattered white dot pattern"></div>
    <div class="back-brand">
      <p class="brand-name">
        <span class="brand-name__line">Varnel</span>
        <span class="brand-name__line">liquid</span>
        <span class="brand-name__line brand-name__line--chalk">CHALK</span>
      </p>
      <span class="back-brand__rule"></span>
    </div>
  </section>

</main>
</body>
</html>
```